Business Card for By Marcus Hale

Looking to have a business card designed for my lifestyle and fitness company. My company offers personal training, online programming and nutrition advice based out of London, United Kingdom.

I'd like to see modern, sleek designs, focusing on black, matte black or matte grey. Design doesn't need to be overly descriptive as this will also be used as a personal business card. I've included my logo.

Please note that my company is no longer called "Fitness by Marcus Hale" but instead "By Marcus Hale", this is because of my other ventures. Therefore please don't use the "fitness by marcus hale" text.

information about my company can be found at www.bymarcushale.com

Company is also based out of London (United Kingdom) & Sydney (Australia) this could be reflected on the card.

Industry/Entity Type

Business

Contact Information for Business Card

Marcus Hale
+44 7382 615204
marcus@bymarcushale.com
www.bymarcushale.com

Font styles to use
Sans Serif

Requirements
Must have
• All contact details and inclusion of my logo.

```html
<!DOCTYPE html>
<html lang="en">
<head>
<meta charset="utf-8">
<title>By Marcus Hale — Business Card</title>
<link href="https://fonts.googleapis.com/css2?family=Arimo:wght@400;700&display=swap" rel="stylesheet">
<style>
  :root {
    --backdrop: #d9d9d9;
    --card-light: #ebebeb;
    --card-dark: #000000;
    --ink-dark: #1a1a1a;
    --ink-light: #ffffff;
    --edge-white: #ffffff;
  }
  * { margin: 0; padding: 0; box-sizing: border-box; }
  html, body {
    width: 1200px; height: 1200px; overflow: hidden;
    background: var(--backdrop);
    font-family: "Arimo", Arial, sans-serif;
  }
  .canvas { position: relative; width: 1200px; height: 1200px; }

  .card { position: absolute; left: 188px; width: 840px; height: 480px; overflow: hidden; }

  /* Front */
  .card--front { top: 66px; background: var(--card-light); }
  .card--front .brand {
    position: absolute; left: 0; right: 0; top: 200px;
    display: flex; align-items: center; justify-content: center; gap: 18px;
    color: var(--ink-dark); font-weight: 700; font-size: 54px; letter-spacing: 1px;
  }
  .brand-dot { width: 30px; height: 30px; border-radius: 50%; background: currentColor; }
  .card--front .base-band {
    position: absolute; left: 0; right: 0; bottom: 0; height: 36px; background: var(--card-dark);
  }

  /* Back */
  .card--back { top: 614px; background: var(--card-dark); color: var(--ink-light); }
  .card--back .side-strip {
    position: absolute; left: 0; top: 0; bottom: 0; width: 42px; background: var(--edge-white);
  }
  .card--back .brand {
    position: absolute; left: 90px; width: 240px; top: 170px;
    display: flex; flex-direction: column; align-items: center; gap: 16px;
    font-weight: 700; font-size: 34px; text-align: center; line-height: 1.15;
  }
  .card--back .brand .brand-dot { width: 44px; height: 44px; }

  .holder-name {
    position: absolute; left: 498px; top: 128px;
    font-weight: 700; font-size: 36px; letter-spacing: 0.5px;
  }
  .rule { position: absolute; right: 0; height: 2px; background: var(--ink-light); }
  .rule--name { left: 498px; top: 176px; }
  .rule--phone { left: 498px; top: 338px; }
  .rule--email { left: 498px; top: 390px; }

  .contact { position: absolute; left: 452px; display: flex; align-items: center; }
  .contact svg { width: 30px; flex: none; }
  .contact span { margin-left: 26px; }
  .contact--phone { top: 300px; font-size: 25px; }
  .contact--email { top: 360px; font-size: 18px; }
  .contact--web { top: 410px; font-size: 18px; }
</style>
</head>
<body>
<div class="canvas">

  <section class="card card--front">
    <div class="brand"><span class="brand-dot"></span>By Marcus Hale</div>
    <div class="base-band"></div>
  </section>

  <section class="card card--back">
    <div class="side-strip"></div>
    <div class="brand"><span class="brand-dot"></span>By Marcus Hale</div>

    <h1 class="holder-name">Marcus Hale</h1>
    <div class="rule rule--name"></div>

    <div class="contact contact--phone">
      <svg viewBox="0 0 30 40" height="40" aria-hidden="true">
        <rect x="6" y="1" width="18" height="38" rx="3" fill="none" stroke="#fff" stroke-width="2"/>
        <line x1="6" y1="7" x2="24" y2="7" stroke="#fff" stroke-width="1.5"/>
        <line x1="6" y1="31" x2="24" y2="31" stroke="#fff" stroke-width="1.5"/>
        <circle cx="15" cy="35" r="1.6" fill="#fff"/>
      </svg>
      <span>+44 7382 615204</span>
    </div>
    <div class="rule rule--phone"></div>

    <div class="contact contact--email">
      <svg viewBox="0 0 30 22" height="22" aria-hidden="true">
        <rect x="1" y="1" width="28" height="20" fill="none" stroke="#fff" stroke-width="1.5"/>
        <polyline points="1,1 15,12 29,1" fill="none" stroke="#fff" stroke-width="1.5"/>
        <polyline points="1,21 11,9 M29,21 19,9" fill="none" stroke="#fff" stroke-width="1.5"/>
      </svg>
      <span>marcus@bymarcushale.com</span>
    </div>
    <div class="rule rule--email"></div>

    <div class="contact contact--web">
      <svg viewBox="0 0 44 22" height="22" style="width:44px;margin-left:-10px" aria-hidden="true">
        <ellipse cx="22" cy="11" rx="20" ry="10" fill="none" stroke="#fff" stroke-width="1.5"/>
        <ellipse cx="22" cy="11" rx="8" ry="10" fill="none" stroke="#fff" stroke-width="1.2"/>
        <line x1="22" y1="1" x2="22" y2="21" stroke="#fff" stroke-width="1.2"/>
        <line x1="2" y1="11" x2="42" y2="11" stroke="#fff" stroke-width="1.2"/>
        <line x1="6" y1="5" x2="38" y2="5" stroke="#fff" stroke-width="1"/>
        <line x1="6" y1="17" x2="38" y2="17" stroke="#fff" stroke-width="1"/>
      </svg>
      <span style="margin-left:16px">www.bymarcushale.com</span>
    </div>
  </section>

</div>
</body>
</html>
```